Copper Vale Winery wants innovative label for unique bottling

We are looking for a lable for a champagne which is made of Eiswein (Ice Wine; this is what you get when you harvest the grapes at temperatures below -7 degrees celsius. the water is frozen and you only get the pure extract out of the grapes (sugar, acid and all the aromas). even after fermentation is remains very sweet. we then turned it into champagne (2nd fermentation in bottles for another 12 months and so on and so forth). It is bottled in small champagne bottles (0,375 l). Dark green (just like a champagne bottle). The name of the product is "Glintova" (from Freeze and Riesling). So it is unique, it is sparkling, it is sweet, it is full of aromas and it is produced from deep frozen grapes. All of this hopefully creates ideas in your imagination which lead to great designs! The only word printed onto the label is "Glintova". The colour code should still be recognizable. See www.brandt-wolmer.de for our standard labels and bottles. you can also download label designs and colours. we prefer modern / fresh / light design rather than traditional, flowery, pittoresque. But please not 100 different colours or screaming colours. You may also imagine transparent labels. Up to you! Have fun!

```html
<!DOCTYPE html>
<html lang="en">
<head>
<meta charset="utf-8">
<title>Glintova label</title>
<link href="https://fonts.googleapis.com/css2?family=Great+Vibes&display=swap" rel="stylesheet">
<style>
  :root {
    --paper: #ffffff;
    --frost: #fbfbf3;
    --chartreuse: #c8c22a;
    --script-faint: #f1f1e6;
    --script-white: #ffffff;
    --glass-dark: #0b0b0b;
    --glass-light: #3c3c3c;
  }
  html, body {
    margin: 0;
    padding: 0;
    overflow: hidden;
    background: var(--paper);
  }
  .canvas {
    position: relative;
    width: 1200px;
    height: 1000px;
    background: var(--paper);
    overflow: hidden;
  }
  .artwork {
    position: absolute;
    inset: 0;
  }
  .label-name {
    font-family: "Great Vibes", cursive;
  }
</style>
</head>
<body>
<div class="canvas">
  <svg class="artwork" width="1200" height="1000" viewBox="0 0 1200 1000" xmlns="http://www.w3.org/2000/svg">
    <defs>
      <linearGradient id="label-fade" x1="0" y1="0" x2="1" y2="0">
        <stop offset="0" stop-color="var(--chartreuse)"/>
        <stop offset="0.18" stop-color="var(--frost)"/>
        <stop offset="0.5" stop-color="var(--paper)"/>
        <stop offset="0.82" stop-color="var(--frost)"/>
        <stop offset="1" stop-color="var(--chartreuse)"/>
      </linearGradient>
      <linearGradient id="glass-shade" x1="0" y1="0" x2="1" y2="0">
        <stop offset="0" stop-color="var(--glass-dark)"/>
        <stop offset="0.3" stop-color="var(--glass-light)"/>
        <stop offset="0.6" stop-color="var(--glass-dark)"/>
        <stop offset="1" stop-color="#2a2a2a"/>
      </linearGradient>
      <linearGradient id="small-label-fade" x1="0" y1="0" x2="1" y2="0">
        <stop offset="0" stop-color="var(--chartreuse)" stop-opacity="0.9"/>
        <stop offset="0.25" stop-color="#ffffff" stop-opacity="0.15"/>
        <stop offset="0.75" stop-color="#ffffff" stop-opacity="0.15"/>
        <stop offset="1" stop-color="var(--chartreuse)" stop-opacity="0.9"/>
      </linearGradient>
    </defs>

    <!-- flat label -->
    <g class="label-flat">
      <ellipse class="label-oval" cx="461" cy="530" rx="298" ry="190" fill="url(#label-fade)"/>
      <rect class="label-band" x="268" y="345" width="80" height="370" fill="#ffffff" opacity="0.35"/>
      <rect class="label-band" x="570" y="345" width="60" height="370" fill="#ffffff" opacity="0.35"/>
      <text class="label-name" x="446" y="565" text-anchor="middle" font-size="150" fill="var(--script-faint)">Glintova</text>
    </g>

    <!-- bottle presentation -->
    <g class="label-on-bottle">
      <rect class="bottle-area" role="img" aria-label="Dark champagne bottle carrying the label"
            x="848" y="95" width="187" height="800" rx="24" fill="url(#glass-shade)"/>
      <ellipse class="label-oval-small" cx="940" cy="513" rx="76" ry="48" fill="url(#small-label-fade)"/>
      <text class="label-name" x="938" y="522" text-anchor="middle" font-size="32" fill="var(--script-white)">Glintova</text>
    </g>
  </svg>
</div>
</body>
</html>
```